" Nós iremos oferecer cursos voltados para a área de controladoria e finanças, desenvolvimento pessoal e empresarial. Ofereceremos também consultoria nestes mesmos ramos. "

```html
<!DOCTYPE html>
<html lang="pt-BR">
<head>
<meta charset="utf-8">
<title>Rumo Treinamentos – Cartão de visita</title>
<link rel="stylesheet" href="https://fonts.googleapis.com/css2?family=Montserrat:ital,wght@0,400;0,500;0,700;1,400&display=swap">
<style>
  :root{
    --navy:#173a5e;
    --navy-deep:#112d4a;
    --gold:#b8924a;
    --gold-light:#d9b873;
    --white:#ffffff;
    --paper:#f7f7f7;
    --backdrop:#e9e6e1;
    --ink-soft:#e8edf3;
  }
  *{margin:0;padding:0;box-sizing:border-box}
  html,body{width:1200px;height:1200px;overflow:hidden}
  body{
    background:var(--backdrop);
    font-family:"Montserrat",sans-serif;
    position:relative;
  }
  .card{
    position:absolute;
    left:160px;
    width:880px;
    height:500px;
    border-radius:22px;
    overflow:hidden;
    box-shadow:0 14px 34px rgba(0,0,0,.18);
  }
  /* front */
  .card--front{top:60px;background:linear-gradient(135deg,var(--white),var(--paper))}
  .front-brand{
    position:absolute;left:50%;top:50%;transform:translate(-50%,-50%);
    display:flex;align-items:center;gap:26px;
  }
  .brand-square{width:120px;height:120px;border-radius:20px;background:var(--gold)}
  .brand-name{color:var(--gold);font-weight:700;line-height:1;text-transform:uppercase}
  .front-brand .brand-word{display:block;font-size:96px;letter-spacing:2px}
  .front-brand .brand-sub{display:block;font-size:26px;letter-spacing:3px;margin-top:8px}

  /* back */
  .card--back{top:620px;background:linear-gradient(160deg,var(--navy),var(--navy-deep));color:var(--white)}
  .name-bar{position:absolute;left:0;top:62px;width:20px;height:44px;background:linear-gradient(90deg,var(--gold),var(--gold-light))}
  .holder-name{position:absolute;left:48px;top:64px;font-size:34px;font-weight:500;letter-spacing:.5px}
  .contact-band{position:absolute;left:0;top:150px;width:52px;height:150px;background:linear-gradient(90deg,var(--gold),var(--gold-light))}
  .contact-list{position:absolute;left:72px;top:150px;list-style:none}
  .contact-list li{display:flex;align-items:center;gap:16px;height:50px;font-size:23px;font-style:italic}
  .contact-list svg{width:22px;height:22px;flex:none}
  .address-line{position:absolute;left:0;top:372px;width:30px;height:3px;background:var(--gold)}
  .address{position:absolute;left:48px;top:356px;font-size:23px;font-style:italic;color:var(--ink-soft)}
  .back-brand{position:absolute;right:60px;top:130px;display:flex;flex-direction:column;align-items:center;gap:16px}
  .back-brand .brand-square{width:90px;height:90px;border-radius:16px}
  .back-brand .brand-word{display:block;font-size:64px;text-align:center}
  .back-brand .brand-sub{display:block;font-size:17px;letter-spacing:2px;margin-top:6px;text-align:center}
</style>
</head>
<body>

<section class="card card--front" aria-label="Frente do cartão">
  <div class="front-brand">
    <div class="brand-square"></div>
    <div class="brand-name"><span class="brand-word">Rumo</span><span class="brand-sub">Treinamentos</span></div>
  </div>
</section>

<section class="card card--back" aria-label="Verso do cartão">
  <div class="name-bar"></div>
  <h1 class="holder-name">Caio Menezes</h1>

  <div class="contact-band"></div>
  <ul class="contact-list">
    <li>
      <svg viewBox="0 0 24 24" aria-hidden="true"><rect x="2" y="2" width="20" height="20" rx="4" fill="#fff"/><path d="M8 6h2l1 3-1.5 1.2a8 8 0 0 0 4.3 4.3L15 13l3 1v2a2 2 0 0 1-2 2A10 10 0 0 1 6 8a2 2 0 0 1 2-2z" fill="#173a5e"/></svg>
      +55 11 0000.0000
    </li>
    <li>
      <svg viewBox="0 0 24 24" aria-hidden="true"><rect x="2" y="2" width="20" height="20" rx="4" fill="#fff"/><circle cx="12" cy="12" r="3" fill="none" stroke="#173a5e" stroke-width="2"/><path d="M15 9v4a2 2 0 0 0 4 0v-1a7 7 0 1 0-3 5.7" fill="none" stroke="#173a5e" stroke-width="2"/></svg>
      caio@rumotreinamentos.com.br
    </li>
    <li>
      <svg viewBox="0 0 24 24" aria-hidden="true"><rect x="2" y="2" width="20" height="20" rx="4" fill="#fff"/><circle cx="12" cy="12" r="6" fill="none" stroke="#173a5e" stroke-width="1.6"/><path d="M6 12h12M12 6c-3 3-3 9 0 12M12 6c3 3 3 9 0 12" fill="none" stroke="#173a5e" stroke-width="1.4"/></svg>
      www.rumotreinamentos.com.br
    </li>
  </ul>

  <div class="address-line"></div>
  <p class="address">Rua das Palmeiras, 210 Sala 8 Centro - São Paulo SP</p>

  <div class="back-brand">
    <div class="brand-square"></div>
    <div class="brand-name"><span class="brand-word">Rumo</span><span class="brand-sub">Treinamentos</span></div>
  </div>
</section>

</body>
</html>
```